Wine Label Design

A wine label for 750ml bottles. Same label for different varieties with the variety / region / vintage to be updated as required.
Brand: Beyond the Ridge
Product Use: Front and Back label suitable for a 750 ml bottle (preferably Burgundy bottles)
Design Brief: Beyond the Ridge is a small winery that produces limited amounts of hand crafted wines that are aimed at the mid to top end of the market and requires a label befitting the work that goes into the creation of the wine. In terms of style i don't have any preconceptions and am open to a broad range of design suggestions at the same level of existing premium brands or innovative brands.
Must Have for Front label
Front Label
Beyond the Ridge
2013
Grampians
Shiraz
750ML (should be in smaller text)
Alc. 14% by Vol. (should be in smaller text)
Must Have for Back Label
Beyond the Ridge
2013
Grampians
Shiraz
www.beyondtheridge.com.au (should be in smaller text)
Product of Australia
Alc.14% by Vol. (should be in smaller text)
Contains preservative 220(should be in smaller text)
Below are some guides for dimensions:
The Front Label Size can be between
100 - 120 mm (Width) x 70 - 85 mm (Height)
The back label size can be between
90 mm (Width) x 70 - 85 mm (Height)
Target Market(s)
Medium to top end of the wine market who require the label to be a reflection of the wine.
Industry/Entity Type
Product
Colors
Designer to choose colors to be used in the design.
Look and feel

```html
<!DOCTYPE html>
<html lang="en">
<head>
<meta charset="utf-8">
<title>Beyond the Ridge – Wine Labels</title>
<link href="https://fonts.googleapis.com/css2?family=Tinos:wght@400;700&display=swap" rel="stylesheet">
<style>
  :root {
    --paper: #ffffff;
    --backdrop: #f6f5f3;
    --ink: #1c1c1c;
    --wine-red: #c4202a;
    --ornament: #8a2f2a;
    --peach: #f6d9b8;
    --vine-green: #7fb98a;
    --hill-tan: #f1c79f;
  }
  * { margin: 0; padding: 0; box-sizing: border-box; }
  html, body {
    width: 1200px; height: 848px; overflow: hidden;
    background: var(--backdrop);
    font-family: "Tinos", "Times New Roman", serif;
    color: var(--ink);
  }
  .canvas { position: relative; width: 1200px; height: 848px; }

  .label {
    position: absolute;
    background: var(--paper);
    box-shadow: 0 2px 10px rgba(0,0,0,0.08);
    overflow: hidden;
  }
  .label > * { position: absolute; }

  .ornament-strip {
    top: 8px; bottom: 8px; width: 14px;
    background: linear-gradient(180deg, #a4544c, var(--ornament), #a4544c);
    opacity: 0.75;
  }
  .ornament-frame {
    inset: 8px;
    border: 10px solid var(--ornament);
    opacity: 0.7;
  }
  .sweep {
    background: radial-gradient(ellipse at 20% 100%, rgba(246,217,184,0.9) 0%, rgba(246,217,184,0.5) 45%, rgba(246,217,184,0) 75%);
  }
  .vineyard-scene {
    left: 50%; transform: translateX(-50%);
    background: linear-gradient(180deg, var(--hill-tan) 0%, #f7e6d2 35%, #a8d4ac 55%, var(--vine-green) 100%);
    border-radius: 40% 40% 8px 8px / 30% 30% 8px 8px;
  }
  .brand {
    left: 0; right: 0; text-align: center;
    text-transform: uppercase; letter-spacing: 0.04em;
    font-weight: 400;
  }
  .info { left: 0; right: 0; text-align: center; line-height: 1.2; }
  .vintage, .region { display: block; }
  .variety {
    display: inline-flex; align-items: center; gap: 6px;
    color: var(--wine-red);
  }
  .variety::before, .variety::after {
    content: ""; display: block; height: 1px; background: var(--wine-red);
  }
  .small-print { left: 0; right: 0; text-align: center; line-height: 1.3; }

  /* Front label */
  .label--front { left: 190px; top: 232px; width: 368px; height: 408px; }
  .label--front .ornament-strip--left { left: 6px; }
  .label--front .ornament-strip--right { right: 6px; }
  .label--front .brand { top: 48px; font-size: 32px; }
  .label--front .vineyard-scene { top: 112px; width: 150px; height: 80px; }
  .label--front .sweep { left: 40px; bottom: 0; width: 320px; height: 150px; }
  .label--front .info { top: 222px; }
  .label--front .vintage { font-size: 21px; }
  .label--front .region { font-size: 27px; letter-spacing: 0.03em; }
  .label--front .variety { font-size: 27px; letter-spacing: 0.02em; }
  .label--front .variety::before, .label--front .variety::after { width: 38px; }
  .label--front .small-print { top: 348px; font-size: 13px; }

  /* Back label */
  .label--back { left: 700px; top: 262px; width: 262px; height: 366px; }
  .label--back .brand { top: 34px; font-size: 17px; }
  .label--back .vineyard-scene { top: 66px; width: 84px; height: 44px; }
  .label--back .sweep { left: 12px; bottom: 12px; width: 220px; height: 120px; }
  .label--back .info { top: 120px; }
  .label--back .vintage { font-size: 11px; }
  .label--back .region { font-size: 13px; letter-spacing: 0.03em; }
  .label--back .variety { font-size: 13px; }
  .label--back .variety::before, .label--back .variety::after { width: 16px; }
  .label--back .web { top: 187px; left: 0; right: 0; text-align: center; font-size: 11px; }
  .label--back .origin { top: 203px; left: 0; right: 0; text-align: center; font-size: 17px; }
  .label--back .small-print { top: 268px; font-size: 11px; }
</style>
</head>
<body>
<main class="canvas">

  <section class="label label--front" aria-label="Front label">
    <div class="ornament-strip ornament-strip--left" role="img" aria-label="Decorative scroll border"></div>
    <div class="ornament-strip ornament-strip--right" role="img" aria-label="Decorative scroll border"></div>
    <div class="sweep" role="img" aria-label="Soft peach curved vineyard row lines"></div>
    <h1 class="brand">Beyond the Ridge</h1>
    <div class="vineyard-scene" role="img" aria-label="Sketch of a vineyard with hills and a farmhouse"></div>
    <div class="info">
      <span class="vintage">2013</span>
      <span class="region">GRAMPIANS</span>
      <span class="variety">SHIRAZ</span>
    </div>
    <p class="small-print">750ML<br>Alc 14% by Vol</p>
  </section>

  <section class="label label--back" aria-label="Back label">
    <div class="ornament-frame" role="img" aria-label="Decorative scroll frame"></div>
    <div class="sweep" role="img" aria-label="Soft peach curved vineyard row lines"></div>
    <h2 class="brand">Beyond the Ridge</h2>
    <div class="vineyard-scene" role="img" aria-label="Sketch of a vineyard with hills and a farmhouse"></div>
    <div class="info">
      <span class="vintage">2013</span>
      <span class="region">GRAMPIANS</span>
      <span class="variety">SHIRAZ</span>
    </div>
    <p class="web">www.beyondtheridge.com.au</p>
    <p class="origin">Product of Australia</p>
    <p class="small-print">750ML<br>Alc 14% by Vol<br>Contains preservative 220</p>
  </section>

</main>
</body>
</html>
```